" O aplicativo coleta informações em campo através de pontos georreferenciados com entrada de detalhes(descrições), fotos e áudio. As informações coletadas em campo são exportadas para ser processadas e assim, gerados dados estatísticos em outra plataforma. "

```html
<!DOCTYPE html>
<html lang="pt-BR">
<head>
<meta charset="utf-8">
<title>Terrix – Coleta em Campo</title>
<link rel="stylesheet" href="https://fonts.googleapis.com/css2?family=Open+Sans:wght@400;700&display=swap">
<style>
  :root {
    --page-bg: #ececec;
    --header-bg: #262626;
    --brand-green: #2f9a3c;
    --tab-bg: #e4e4e4;
    --tab-text: #333333;
    --tile-orange: #f5941f;
    --tile-text: #ffffff;
    --grid-bg: #ffffff;
    --footer-bg: #1f1f1f;
    --footer-text: #e6e6e6;
  }
  * { box-sizing: border-box; margin: 0; padding: 0; }
  html, body {
    width: 1200px; height: 1200px; overflow: hidden;
    background: var(--page-bg);
    font-family: "Open Sans", Arial, sans-serif;
  }
  .app-screen {
    position: absolute; left: 220px; top: 70px;
    width: 760px; height: 1060px;
    display: flex; flex-direction: column;
    background: var(--grid-bg);
    box-shadow: 0 10px 40px rgba(0,0,0,.15);
  }
  .app-header {
    height: 110px; background: var(--header-bg);
    display: flex; align-items: center; padding: 0 26px 0 0;
  }
  .brand-mark {
    width: 110px; height: 110px; background: var(--brand-green);
  }
  .app-title {
    color: #ffffff; font-weight: 700; font-size: 30px; margin-left: 24px; flex: 1;
  }
  .header-actions { display: flex; gap: 16px; }
  .action-button {
    width: 62px; height: 62px; border-radius: 50%;
    border: 3px solid #ffffff; display: flex; align-items: center; justify-content: center;
    color: #ffffff; font-weight: 700; font-size: 28px;
  }
  .tab-bar { height: 64px; display: flex; }
  .tab {
    flex: 1; display: flex; align-items: center; justify-content: center;
    background: var(--tab-bg); color: var(--tab-text);
    font-weight: 700; font-size: 17px; text-transform: uppercase;
    border-left: 2px solid #ffffff;
  }
  .tab.is-active { background: var(--brand-green); color: #ffffff; border-left: none; }
  .tile-grid {
    flex: 1; padding: 24px 26px; display: flex; flex-direction: column; gap: 14px;
  }
  .tile-row { flex: 1; display: flex; gap: 14px; }
  .tile {
    flex: 1; background: var(--tile-orange); color: var(--tile-text);
    display: flex; align-items: center; justify-content: center; text-align: center;
    font-weight: 700; font-size: 19px; padding: 0 6px;
  }
  .app-footer {
    height: 60px; background: var(--footer-bg); color: var(--footer-text);
    display: flex; align-items: center; justify-content: center; font-size: 18px;
  }
</style>
</head>
<body>
  <main class="app-screen">
    <header class="app-header">
      <div class="brand-mark"></div>
      <h1 class="app-title">Terrix</h1>
      <nav class="header-actions">
        <span class="action-button">P</span>
        <span class="action-button">
          <svg width="24" height="24" viewBox="0 0 24 24"><polygon points="6,3 21,12 6,21" fill="#fff"/></svg>
        </span>
        <span class="action-button">
          <svg width="24" height="24" viewBox="0 0 24 24" fill="#fff">
            <rect x="2" y="2" width="9" height="9"/><rect x="13" y="2" width="9" height="9"/>
            <rect x="2" y="13" width="9" height="9"/><rect x="13" y="13" width="9" height="9"/>
          </svg>
        </span>
      </nav>
    </header>

    <div class="tab-bar">
      <div class="tab is-active">Lado Esquerdo</div>
      <div class="tab">Plataforma</div>
      <div class="tab">Lado Direito</div>
    </div>

    <section class="tile-grid">
      <div class="tile-row">
        <div class="tile">Sin. Fax.</div><div class="tile">Acesso</div><div class="tile">Portaria</div><div class="tile">M. Bueiro</div>
      </div>
      <div class="tile-row">
        <div class="tile">Cer. Água</div><div class="tile">Sarjeta</div><div class="tile">Muro In</div><div class="tile">Des. Água</div>
      </div>
      <div class="tile-row">
        <div class="tile">Placa</div><div class="tile">Pórtico</div><div class="tile">Defensa</div><div class="tile">N. Jersey</div>
      </div>
      <div class="tile-row">
        <div class="tile">Árvore @ 15</div><div class="tile">Árvore @ 30</div><div class="tile">Vegetação APP</div>
      </div>
      <div class="tile-row">
        <div class="tile">Poste AT</div><div class="tile">Poste BT</div><div class="tile">Torre</div><div class="tile">R. Elétrico</div>
      </div>
      <div class="tile-row">
        <div class="tile">Edificação</div><div class="tile">Escola</div><div class="tile">Ponto de Ônibus</div>
      </div>
    </section>

    <footer class="app-footer">© Aplicativo Terrix</footer>
  </main>
</body>
</html>
```